Gulf Powerfair Infographic

We need to have an Infographic designed that displays statistics about the energy sector in Saudi Arabia.

We are an exhibitions organiser but we only want to link it back to the exhibition, Gulf Powerfair, by including our logo in the corner under the title 'Created by' (the logo is attached). The rest of the information and design needs to be entirely related to the industry and not the exhibition at all.

The objective of the Infographic is to convey the hard facts about a serious topic in an easy to digest manner. I have attached a word document with a few Infographic designs that we like.

We are using the Infographic for digital designs only so please make sure the Infographic fits onto a web screen easily and there is no need to scroll to see the information but other than that we are relatively flexible on the size.

The content is as follows but please feel free to interpret the content rather than copy word for word:
- Electricity consumption in Saudi Arabia increased sharply during the 1990–2010 period due to rapid economic development. Peak loads reached nearly 24 GW in 2001—25 times their 1975 level-and are expected to approach 60 GW by 2023
- The investment needed to meet this demand may exceed $90 billion. Consequently, there is an urgent need to develop energy conservation policies for sustainable development
- Generation capacity is approximately 55 GW. A looming energy shortage requires Saudi Arabia to increase its capacity. Capacity is planned to be increased to 120 GW by 2020.
- The government has approved the construction of a $300 million facility to turn waste into energy. The facility will process 180 tons of waste per day, producing 6 MW of electricity and 250,000 US gallons (950 m3) of distilled water.
- If energy conservation is successful, demand can be reduced by 5–10%. This is equivalent to 3–6 GW of additional capacity, which represents a possible $1.5–3.0 billion saving over 20 years.
- Saudi Arabia, has said it hopes to generate solar power of up to 41GW by 2032, or 30 per cent of peak power demand. That is almost double the current capacity of Germany, the world’s leading solar power.
- Saudi Arabia will invest in 17 new nuclear reactors in next 20 years.
- Coastal Brine Treatment Authority needs to increase desalinated water supply to 8.5m cubic metres a day by 2025
- Saudi Arabia is building the world’s largest solar-powered desalination plant at Khafji, which will produce 30,000 cubic metres a day of water once it is completed in the next two years. All power and water plants built from 2020 onwards will run on solar energy, NOVRA’s Prince Halvan said.
- Construction projects worth $75.6bn in Saudi Arabia during 2014, over 10% increase from 2013, $195.4 billion worth of construction planned in Saudi Arabia in the coming three years, and a further over $1 trillion worth of projects planned or under construction

Feel free to post any questions about this project and I will get back to you as soon as possible.

I look forward to seeing your designs!

```html
<!DOCTYPE html>
<html lang="en">
<head>
<meta charset="utf-8">
<title>Energy Sector in Saudi Arabia</title>
<link rel="stylesheet" href="https://fonts.googleapis.com/css2?family=Montserrat:wght@800;900&family=Open+Sans:wght@400;700;800&display=swap">
<style>
:root{
  --sand:#e9e2cf;
  --charcoal:#3b3a39;
  --ink:#2f2e2d;
  --coral:#ec4d4f;
  --teal:#3ab3c4;
  --text:#e9e2cf;
}
*{box-sizing:border-box;margin:0;padding:0}
html,body{width:1200px;height:4235px;overflow:hidden;background:var(--charcoal)}
.infographic{position:relative;width:1200px;height:4235px;background:var(--charcoal);font-family:"Open Sans",Arial,sans-serif;overflow:hidden}
.masthead{position:absolute;left:0;top:0;width:1200px;height:760px;background:var(--sand)}
.title{position:absolute;left:100px;top:385px;color:var(--ink);font-family:"Montserrat",Arial,sans-serif;font-weight:900;line-height:.9}
.title .line-1{display:block;font-size:128px;letter-spacing:2px}
.title .line-2{display:block;font-size:80px;letter-spacing:3px;margin-top:6px}
.title .line-3{display:block;font-size:33px;letter-spacing:2px;margin-top:14px;font-weight:800}
.rig-art{position:absolute;left:690px;top:210px;width:510px;height:550px;background:linear-gradient(180deg,rgba(59,58,57,.15) 0%,rgba(59,58,57,.55) 55%,var(--charcoal) 100%);clip-path:polygon(38% 0,46% 0,52% 45%,100% 45%,100% 100%,0 100%,0 62%,30% 62%)}
.spine{position:absolute;left:898px;top:760px;width:0;height:3350px;border-left:4px dashed var(--sand);opacity:.9}
.fact{position:absolute;left:0;width:1200px;height:300px}
.fact-text{position:absolute;left:106px;top:50%;transform:translateY(-50%);width:610px;color:var(--text);font-size:22px;line-height:1.38}
.coral{color:var(--coral);font-weight:800}
.teal{color:var(--teal);font-weight:800}
.badge{position:absolute;left:760px;top:10px;width:280px;height:280px}
.footer{position:absolute;left:0;bottom:0;width:1200px;height:125px;background:var(--sand);display:flex;align-items:center;justify-content:center;gap:22px;color:var(--ink)}
.footer .credit{font-size:30px;font-weight:800}
.brand{display:flex;align-items:center;gap:12px;font-size:34px;font-weight:800;color:var(--ink)}
.brand .mark{width:30px;height:30px;border-radius:50%;background:var(--coral)}
</style>
</head>
<body>
<main class="infographic">
  <header class="masthead">
    <h1 class="title"><span class="line-1">ENERGY</span><span class="line-2">SECTOR</span><span class="line-3">IN SAUDI ARABIA</span></h1>
    <div class="rig-art" role="img" aria-label="Silhouette of an offshore oil rig with derrick and cranes"></div>
  </header>

  <div class="spine"></div>

  <section class="fact" style="top:732px">
    <p class="fact-text">Electricity consumption in Saudi Arabia increased sharply during the <span class="coral">1990–2010</span> period due to rapid <span class="teal">economic development</span>. Peak loads reached nearly <span class="coral">24 GW</span> in 2001—25 times their 1975 level-and are expected to approach <span class="coral">60 GW</span> by 2023</p>
    <svg class="badge" viewBox="0 0 280 280" aria-hidden="true"><circle cx="140" cy="140" r="136" fill="none" stroke="var(--sand)" stroke-width="3" stroke-dasharray="6 6"/><circle cx="140" cy="140" r="124" fill="var(--sand)"/>
      <g stroke="var(--charcoal)" stroke-width="7" fill="none" stroke-linecap="round"><path d="M110 215V80M90 95h90M110 80l-25 15M180 95v40"/><path d="M165 215V120M150 130h60M165 120l-20 10M205 130v30"/><path d="M75 215h130"/></g></svg>
  </section>

  <section class="fact" style="top:1068px">
    <p class="fact-text">The investment needed to meet this demand may exceed <span class="coral">$90 billion</span>. Consequently, there is an urgent need to develop <span class="teal">energy conservation</span> policies for sustainable development</p>
    <svg class="badge" viewBox="0 0 280 280" aria-hidden="true"><circle cx="140" cy="140" r="136" fill="none" stroke="var(--sand)" stroke-width="3" stroke-dasharray="6 6"/><circle cx="140" cy="140" r="124" fill="var(--sand)"/>
      <g fill="var(--charcoal)"><path d="M136 125h8l6 100h-20z"/><circle cx="140" cy="120" r="9"/><path d="M137 117L200 55l6 6-62 62zM134 123l-75 20-2-8 75-20zM146 125l20 75-8 3-20-75z"/></g></svg>
  </section>

  <section class="fact" style="top:1403px">
    <p class="fact-text"><span class="teal">Generation capacity</span> is approximately <span class="coral">55 GW</span>. A looming energy shortage requires Saudi Arabia to increase its capacity. Capacity is planned to be increased to <span class="coral">120 GW</span> by 2020</p>
    <svg class="badge" viewBox="0 0 280 280" aria-hidden="true"><circle cx="140" cy="140" r="136" fill="none" stroke="var(--sand)" stroke-width="3" stroke-dasharray="6 6"/><circle cx="140" cy="140" r="124" fill="var(--sand)"/>
      <g fill="var(--charcoal)"><path d="M60 105h150v70H60z M68 113v54h134v-54z" fill-rule="evenodd"/><rect x="210" y="125" width="12" height="30"/><rect x="76" y="120" width="16" height="40"/><rect x="98" y="120" width="16" height="40"/><rect x="120" y="120" width="16" height="40"/><rect x="142" y="120" width="16" height="40"/><rect x="164" y="120" width="16" height="40"/></g></svg>
  </section>

  <section class="fact" style="top:1738px">
    <p class="fact-text"><span class="teal">The government</span> has approved the construction of a <span class="coral">$300 million</span> facility to turn waste into energy. The facility will process <span class="coral">180 tons</span> of waste per day, producing <span class="coral">6 MW</span> of electricity and <span class="coral">250,000</span> US gallons (950 m3) of distilled water</p>
    <svg class="badge" viewBox="0 0 280 280" aria-hidden="true"><circle cx="140" cy="140" r="136" fill="none" stroke="var(--sand)" stroke-width="3" stroke-dasharray="6 6"/><circle cx="140" cy="140" r="124" fill="var(--sand)"/>
      <g stroke="var(--charcoal)" stroke-width="7" fill="none" stroke-linecap="round"><circle cx="140" cy="128" r="36"/><path d="M124 170h32M128 184h24M140 60v-12M140 208v0M72 128H58M222 128h-14M92 80l-10-10M188 80l10-10M92 176l-10 10M188 176l10 10"/></g><circle cx="140" cy="128" r="14" fill="var(--charcoal)"/></svg>
  </section>

  <section class="fact" style="top:2056px">
    <p class="fact-text">If <span class="teal">energy conservation</span> is successful, demand can be reduced by <span class="coral">5–10%</span>. This is equivalent to <span class="coral">3–6 GW</span> of additional capacity, which represents a possible <span class="coral">$1.5–3.0 billion</span> saving over 20 years</p>
    <svg class="badge" viewBox="0 0 280 280" aria-hidden="true"><circle cx="140" cy="140" r="136" fill="none" stroke="var(--sand)" stroke-width="3" stroke-dasharray="6 6"/><circle cx="140" cy="140" r="124" fill="var(--sand)"/>
      <g fill="none" stroke="var(--charcoal)"><circle cx="115" cy="165" r="30" stroke-width="18" stroke-dasharray="11 8"/><circle cx="115" cy="165" r="12" stroke-width="8"/><circle cx="180" cy="100" r="22" stroke-width="14" stroke-dasharray="9 7"/><circle cx="180" cy="100" r="8" stroke-width="6"/></g></svg>
  </section>

  <section class="fact" style="top:2391px">
    <p class="fact-text"><span class="teal">Saudi Arabia</span>, has said it hopes to generate <span class="coral">solar power</span> of up to <span class="coral">41GW</span> by 2032, or 30 per cent of peak power demand. That is almost double the current capacity of Germany, the world’s leading solar power.</p>
    <svg class="badge" viewBox="0 0 280 280" aria-hidden="true"><circle cx="140" cy="140" r="136" fill="none" stroke="var(--sand)" stroke-width="3" stroke-dasharray="6 6"/><circle cx="140" cy="140" r="124" fill="var(--sand)"/>
      <g stroke="var(--charcoal)" stroke-width="7" fill="none" stroke-linecap="round"><circle cx="140" cy="140" r="36"/><path d="M140 80V64M140 200v16M80 140H64M200 140h16M98 98L86 86M182 98l12-12M98 182l-12 12M182 182l12 12"/></g></svg>
  </section>

  <section class="fact" style="top:2726px">
    <p class="fact-text"><span class="teal">Saudi Arabia</span> will invest in<br><span class="coral">17 new nuclear reactors</span> in next <span class="coral">20 years</span></p>
    <svg class="badge" viewBox="0 0 280 280" aria-hidden="true"><circle cx="140" cy="140" r="136" fill="none" stroke="var(--sand)" stroke-width="3" stroke-dasharray="6 6"/><circle cx="140" cy="140" r="124" fill="var(--sand)"/>
      <g stroke="var(--charcoal)" stroke-width="6" fill="none"><ellipse cx="140" cy="140" rx="75" ry="28"/><ellipse cx="140" cy="140" rx="75" ry="28" transform="rotate(60 140 140)"/><ellipse cx="140" cy="140" rx="75" ry="28" transform="rotate(-60 140 140)"/></g><circle cx="140" cy="140" r="11" fill="var(--charcoal)"/></svg>
  </section>

  <section class="fact" style="top:3044px">
    <p class="fact-text"><span class="teal">Coastal Brine Treatment Authority</span> needs to increase desalinated water supply to <span class="coral">8.5m</span> cubic metres a day by 2025</p>
    <svg class="badge" viewBox="0 0 280 280" aria-hidden="true"><circle cx="140" cy="140" r="136" fill="none" stroke="var(--sand)" stroke-width="3" stroke-dasharray="6 6"/><circle cx="140" cy="140" r="124" fill="var(--sand)"/>
      <g fill="var(--charcoal)"><path d="M70 120c30-40 90-50 140-35-40 0-90 10-140 35z"/><path d="M62 150c45-30 110-40 160-20-55-5-105 5-160 20z"/><path d="M75 180c40-25 100-30 140-15-45 0-95 5-140 15z"/></g></svg>
  </section>

  <section class="fact" style="top:3380px">
    <p class="fact-text"><span class="teal">Saudi Arabia</span> is building the world’s largest <span class="coral">solar-powered desalination</span> plant at Khafji, which will produce <span class="coral">30,000</span> cubic metres a day of water once it is completed in the next two years. All power and water plants built from 2020 onwards will run on solar energy, NOVRA’s Prince Halvan said</p>
    <svg class="badge" viewBox="0 0 280 280" aria-hidden="true"><circle cx="140" cy="140" r="136" fill="none" stroke="var(--sand)" stroke-width="3" stroke-dasharray="6 6"/><circle cx="140" cy="140" r="124" fill="var(--sand)"/>
      <g stroke="var(--charcoal)" stroke-width="12" fill="none" stroke-linecap="round"><path d="M108 100a50 50 0 1 0 64 0"/><path d="M140 80v55"/></g></svg>
  </section>

  <section class="fact" style="top:3715px">
    <p class="fact-text"><span class="teal">Construction projects</span> worth <span class="coral">$75.6bn</span> in Saudi Arabia during 2014, over <span class="coral">10%</span> increase from 2013, <span class="coral">$195.4</span> billion worth of construction planned in <span class="teal">Saudi Arabia</span> in the coming three years, and a further over $1 trillion worth of projects planned or under construction</p>
    <svg class="badge" viewBox="0 0 280 280" aria-hidden="true"><circle cx="140" cy="140" r="136" fill="none" stroke="var(--sand)" stroke-width="3" stroke-dasharray="6 6"/><circle cx="140" cy="140" r="124" fill="var(--sand)"/>
      <g stroke="var(--charcoal)" stroke-width="6" fill="var(--sand)"><path d="M85 190l40-50 30 30 40-70" fill="none"/><circle cx="85" cy="190" r="10"/><circle cx="125" cy="140" r="10"/><circle cx="155" cy="170" r="10"/><circle cx="195" cy="100" r="10"/></g></svg>
  </section>

  <footer class="footer">
    <span class="credit">Created by</span>
    <span class="brand"><span class="mark"></span>Gulf Powerfair</span>
  </footer>
</main>
</body>
</html>
```